Get me out of Jail business cards!!!!

I need business cards done for my business. I own a BailBonds and I get people out of jail!

Colors are red white and black

I need it to say on the card these details:

Freedom Hop Bailbonds

427 S Calloway St
Oak Ridge, FL 34290

863-555-0187

Open 24/7

On the back of the card:

Must check in every Tuesday.

______/______/______ court date
____________________ time
You must know your court date at all times!

Marla Whitcombe - owner
Jolene Whitcombe - agent
Rosalind Pickett - agent

Industry/Entity Type

Bail bonds

Contact Information for Business Card

Colors are red white and black I need it to say on the card these details: Freedom Hop Bailbonds 427 S Calloway St Oak Ridge, FL 34290 863-555-0187 Open 24/7 On the back of the card: Must check in every Tuesday. ______/______/______ court date ____________________ time You must know your court date at all times! Marla Whitcombe - owner Jolene Whitcombe - agent Rosalind Pickett - agent

Font styles to use
Serif
Sans Serif

Colors
EB3D1F
EC4F4E
F09395
F8D3D4
FCEDEE

Requirements
Must have
• I listed the must haves in the business card details
Nice to have
• Handcuffs or jail bars or a man in a black and white suit

```html
<!DOCTYPE html>
<html lang="en">
<head>
<meta charset="utf-8">
<title>Freedom Hop Bailbonds – Business Cards</title>
<link rel="stylesheet" href="https://fonts.googleapis.com/css2?family=Questrial&display=swap">
<style>
  :root {
    --red: #ee0606;
    --ink: #111111;
    --paper: #f7f7f7;
    --backdrop: #e6e3df;
    --white: #ffffff;
  }
  * { box-sizing: border-box; margin: 0; padding: 0; }
  html, body {
    width: 1200px; height: 900px; overflow: hidden;
    background: var(--backdrop);
    font-family: "Questrial", "Century Gothic", sans-serif;
    color: var(--ink);
  }
  .card {
    position: absolute; left: 250px;
    width: 700px; height: 400px;
    background: var(--paper);
    box-shadow: 0 6px 18px rgba(0,0,0,0.15);
    overflow: hidden;
  }
  .card--back { top: 35px; }
  .card--front { top: 465px; }

  .brand-name {
    font-size: 46px; font-weight: 400; color: var(--ink);
    letter-spacing: 0.5px; white-space: nowrap;
  }

  /* Back side */
  .card--back .brand-name {
    position: absolute; top: 36px; left: 0; right: 0; text-align: center;
  }
  .checkin-note {
    position: absolute; top: 125px; left: 0; right: 0;
    text-align: center; font-size: 21px; letter-spacing: 1px;
  }
  .form-row {
    position: absolute; left: 70px; right: 70px;
    display: flex; align-items: flex-end; gap: 14px;
    font-size: 20px; letter-spacing: 1px;
  }
  .form-row--date { top: 185px; }
  .form-row--time { top: 242px; }
  .form-label { width: 120px; text-align: right; flex: none; }
  .fill-line { border-bottom: 2px solid var(--ink); height: 22px; }
  .fill-line--short { width: 120px; }
  .fill-line--mid { width: 150px; }
  .fill-line--end { width: 80px; }
  .tick-box {
    width: 26px; height: 26px; border: 2px solid var(--ink); border-radius: 3px;
    flex: none; margin-left: 12px;
  }
  .band-reminder {
    position: absolute; left: 0; right: 0; bottom: 0; height: 78px;
    background: var(--red); color: var(--white);
    display: flex; align-items: center; justify-content: center;
    font-size: 23px; letter-spacing: 1px;
  }

  /* Front side */
  .card--front .brand-name { position: absolute; top: 36px; left: 80px; }
  .name-row {
    position: absolute; top: 140px; left: 75px; right: 25px;
    display: flex; align-items: flex-start; gap: 12px;
  }
  .rule { border-top: 2px solid var(--ink); }
  .rule--lead { flex: 1; margin-top: 22px; }
  .rule--tail { width: 45px; margin-top: 30px; }
  .person { display: flex; flex-direction: column; }
  .person-name { font-size: 34px; letter-spacing: 1px; white-space: nowrap; line-height: 1.2; }
  .person-role { font-size: 21px; color: var(--red); letter-spacing: 1px; line-height: 1.2; }
  .contact {
    position: absolute; left: 70px;
    display: flex; align-items: flex-start; gap: 16px;
    font-size: 26px; letter-spacing: 2px; line-height: 1.25;
  }
  .contact--phone { top: 240px; }
  .contact--address { top: 292px; }
  .contact-icon { width: 24px; height: 28px; flex: none; margin-top: 2px; fill: var(--red); }
  .tab-hours {
    position: absolute; right: 0; bottom: 28px;
    width: 215px; height: 56px;
    background: var(--red); color: var(--white);
    border-radius: 6px 0 0 6px;
    display: flex; align-items: center; justify-content: center;
    font-size: 29px; letter-spacing: 2px;
  }
</style>
</head>
<body>

<section class="card card--back" aria-label="Card back">
  <div class="brand-name">Freedom Hop Bailbonds</div>
  <p class="checkin-note">Must check in every Tuesday.</p>
  <div class="form-row form-row--date">
    <span class="form-label">Court Date</span>
    <span class="fill-line fill-line--mid"></span>
    <span class="fill-line fill-line--mid"></span>
    <span>20</span>
    <span class="fill-line fill-line--end"></span>
  </div>
  <div class="form-row form-row--time">
    <span class="form-label">Time</span>
    <span class="fill-line fill-line--mid"></span>
    <span class="fill-line fill-line--short"></span>
    <span class="tick-box"></span><span>AM</span>
    <span class="tick-box"></span><span>PM</span>
  </div>
  <div class="band-reminder">You must know your court date at all times!</div>
</section>

<section class="card card--front" aria-label="Card front">
  <div class="brand-name">Freedom Hop Bailbonds</div>
  <div class="name-row">
    <span class="rule rule--lead"></span>
    <div class="person">
      <span class="person-name">Marla Whitcombe</span>
      <span class="person-role">Owner</span>
    </div>
    <span class="rule rule--tail"></span>
  </div>

  <div class="contact contact--phone">
    <svg class="contact-icon" viewBox="0 0 24 24" aria-hidden="true">
      <path d="M6.6 10.8a15.1 15.1 0 0 0 6.6 6.6l2.2-2.2a1 1 0 0 1 1-.25 11.4 11.4 0 0 0 3.6.57 1 1 0 0 1 1 1V20a1 1 0 0 1-1 1A17 17 0 0 1 3 4a1 1 0 0 1 1-1h3.5a1 1 0 0 1 1 1c0 1.25.2 2.45.57 3.57a1 1 0 0 1-.25 1z"/>
    </svg>
    <span>863-555-0187</span>
  </div>
  <div class="contact contact--address">
    <svg class="contact-icon" viewBox="0 0 24 24" aria-hidden="true">
      <path d="M12 2a7 7 0 0 0-7 7c0 5.2 7 13 7 13s7-7.8 7-13a7 7 0 0 0-7-7zm0 9.5A2.5 2.5 0 1 1 12 6.5a2.5 2.5 0 0 1 0 5z"/>
    </svg>
    <span>427 S Calloway St<br>Oak Ridge, FL 34290</span>
  </div>

  <div class="tab-hours">Open 24/7</div>
</section>

</body>
</html>
```